Business card design needed

My company specialises in carpentry and building services.
Based in Brisbane QLD
We also do:
property maintenance
plastering
painting
tiling
property maintenance

Industry/Entity Type

Carpentry

Contact Information for Business Card

ND Services QLD
Neil 0412555783
Derek 0493721068

```html
<!DOCTYPE html>
<html lang="en">
<head>
<meta charset="utf-8">
<title>ND Services — Business Card</title>
<link rel="stylesheet" href="https://fonts.googleapis.com/css2?family=Bowlby+One&family=Cormorant+Garamond:ital,wght@0,600;1,500&family=Marcellus&family=Oswald:wght@500&family=Ubuntu:wght@700&display=swap">
<style>
  :root {
    --wood-light: #8a6a4f;
    --wood-mid: #5e4331;
    --wood-dark: #2b1a12;
    --ink-brown: #3b2217;
    --panel-grey: rgba(196, 190, 184, 0.42);
    --strip-brown: rgba(45, 26, 18, 0.88);
    --box-brown: #2e1c15;
    --cream: #f1e9df;
  }
  html, body {
    margin: 0;
    padding: 0;
    overflow: hidden;
    background: #1c120d;
  }
  .card {
    position: relative;
    width: 1200px;
    height: 695px;
    overflow: hidden;
    background: var(--wood-dark);
  }
  .card__wood {
    position: absolute;
    inset: 0;
    background:
      radial-gradient(ellipse 48% 55% at 50% 26%, rgba(190, 150, 115, 0.55), transparent 70%),
      radial-gradient(ellipse 70% 40% at 50% 92%, rgba(150, 115, 85, 0.45), transparent 75%),
      linear-gradient(90deg, #2a1912 0%, var(--wood-mid) 22%, var(--wood-light) 50%, var(--wood-mid) 78%, #2a1912 100%);
  }
  .brand {
    position: absolute;
    top: 205px;
    left: 0;
    width: 100%;
    margin: 0;
    text-align: center;
    font-family: "Bowlby One", "Arial Black", sans-serif;
    font-weight: 400;
    font-size: 104px;
    line-height: 1;
    letter-spacing: 1px;
    color: var(--wood-dark);
  }
  .location {
    position: absolute;
    top: 352px;
    left: 0;
    width: 100%;
    margin: 0;
    text-align: center;
    font-family: "Cormorant Garamond", serif;
    font-style: italic;
    font-weight: 500;
    font-size: 24px;
    color: var(--ink-brown);
  }
  .contact-panel {
    position: absolute;
    top: 430px;
    left: 0;
    width: 100%;
    height: 151px;
    background: var(--panel-grey);
  }
  .contact-lines {
    position: absolute;
    top: 0;
    left: 0;
  }
  .contact {
    position: absolute;
    top: 452px;
    margin: 0;
    white-space: nowrap;
    color: var(--ink-brown);
  }
  .contact--left { left: 170px; }
  .contact--right { right: 152px; }
  .contact__name {
    font-family: "Ubuntu", sans-serif;
    font-weight: 700;
    font-size: 32px;
  }
  .contact__phone {
    font-family: "Cormorant Garamond", serif;
    font-weight: 600;
    font-size: 30px;
    margin-left: 6px;
  }
  .specialty {
    position: absolute;
    top: 516px;
    left: 395px;
    width: 410px;
    height: 56px;
    margin: 0;
    display: flex;
    align-items: center;
    justify-content: center;
    gap: 9px;
    background: var(--box-brown);
    color: var(--cream);
  }
  .specialty__lead {
    font-family: "Cormorant Garamond", serif;
    font-style: italic;
    font-weight: 500;
    font-size: 24px;
  }
  .specialty__trade {
    font-family: "Oswald", sans-serif;
    font-weight: 500;
    font-size: 21px;
    transform: scaleX(0.86);
    transform-origin: left center;
    margin-right: -36px;
  }
  .services {
    position: absolute;
    top: 581px;
    left: 0;
    width: 100%;
    height: 56px;
    margin: 0;
    display: flex;
    align-items: center;
    justify-content: center;
    background: var(--strip-brown);
    font-family: "Marcellus", serif;
    font-size: 17px;
    color: var(--cream);
    letter-spacing: 0.2px;
  }
</style>
</head>
<body>
  <main class="card">
    <div class="card__wood" role="img" aria-label="Warm wooden plank wall and floor background"></div>

    <h1 class="brand">ND Services</h1>
    <p class="location">Brisbane . Queensland</p>

    <div class="contact-panel"></div>

    <svg class="contact-lines" width="1200" height="695" viewBox="0 0 1200 695" aria-hidden="true">
      <line x1="168" y1="492" x2="1047" y2="492" stroke="#3b2217" stroke-width="4"/>
      <line x1="600" y1="492" x2="600" y2="581" stroke="#3b2217" stroke-width="6"/>
    </svg>

    <p class="contact contact--left">
      <span class="contact__name">Neil</span><span class="contact__phone">0412555783</span>
    </p>
    <p class="contact contact--right">
      <span class="contact__name">Derek</span><span class="contact__phone">0493721068</span>
    </p>

    <p class="specialty">
      <span class="specialty__lead">Specialized in</span>
      <span class="specialty__trade">Carpentry &amp; Building Services</span>
    </p>

    <p class="services">PROPERTY MAINTENANCE . PLASTERING . PAINTING . TILING . PROPERTY MAINTENANCE</p>
  </main>
</body>
</html>
```